Business Card Design Project

This design is a slimline business card 45mm x90mm, the card will be printed at 49mm x 94mm and cut to 45mm x90 mm, this needs to be considered in the design. The content required on the front and back of the business card is attached in a pdf; the design will be done using photo shop as we use CS6 in our business. The design needs to be developed using a CMYK colour pallet, the main colours used on our business are red, grey black and white. A snapshot of our business brochure and new website has been provided to give you an understanding on our businesses look and feel.
FRONT OF BUSINESS CARD
Director
Marcus Feld
Ph+61 0421780213
www.brightvanecontracting.com.au
marcusfeld@brightvanecontracting.com.au
BACK OF BUSINESS CARD
SUPPORTING CLIENTS IN
Oil & Gas I Minerals & Metals I Petrochemical I Manufacturing
Building & Construction I Telecommunication I Rail I Civil I New Industries
KNOWLEDGE I EXPERTISE I EXPERIENCE I CAPACITY

```html
<!DOCTYPE html>
<html lang="en">
<head>
<meta charset="utf-8">
<title>Brightvane Contracting – Business Cards</title>
<link href="https://fonts.googleapis.com/css2?family=Open+Sans:wght@400;600&display=swap" rel="stylesheet">
<style>
  :root {
    --red: #e8232f;
    --red-deep: #c4141f;
    --ink: #111111;
    --grey: #8a8a8a;
    --paper: #ffffff;
    --backdrop: #d9d9d9;
  }
  * { box-sizing: border-box; margin: 0; padding: 0; }
  html, body { width: 1200px; height: 1104px; overflow: hidden; }
  body {
    background: var(--backdrop);
    font-family: "Open Sans", Arial, sans-serif;
    color: var(--ink);
    position: relative;
  }
  .card {
    position: absolute;
    top: 417px;
    width: 540px;
    height: 270px;
    background: var(--paper);
    overflow: hidden;
    box-shadow: 0 2px 6px rgba(0,0,0,.18);
  }
  .card--back { left: 40px; }
  .card--front { left: 620px; }

  .brand { position: absolute; display: flex; align-items: center; }
  .brand__dot { border-radius: 50%; background: var(--red); flex: none; }
  .brand__name { color: var(--ink); font-weight: 400; white-space: nowrap; }
  .brand__tagline {
    position: absolute; font-size: 9.5px; color: var(--ink); white-space: nowrap;
  }

  /* back */
  .card--back .brand { left: 78px; top: 52px; }
  .card--back .brand__dot { width: 46px; height: 46px; margin-right: 14px; }
  .card--back .brand__name { font-size: 30px; letter-spacing: .5px; }
  .card--back .brand__tagline { left: 138px; top: 103px; }
  .sectors {
    position: absolute; left: 0; top: 166px; width: 100%; height: 78px;
    background: linear-gradient(90deg, var(--red-deep), var(--red) 60%, #f03a44);
    color: var(--ink); padding: 12px 0 0 27px; font-size: 13.5px; line-height: 19px;
  }
  .sectors__lead { font-size: 13px; }
  .sectors__list { letter-spacing: .6px; }
  .values {
    position: absolute; left: 0; top: 244px; width: 100%; text-align: center;
    font-size: 15px; line-height: 26px; letter-spacing: .2px;
  }

  /* front */
  .card--front .brand { left: 32px; top: 30px; }
  .card--front .brand__dot { width: 34px; height: 34px; margin-right: 10px; }
  .card--front .brand__name { font-size: 21px; }
  .card--front .brand__tagline { left: 76px; top: 75px; font-size: 7.5px; }
  .person { position: absolute; right: 30px; top: 48px; text-align: right; }
  .person__name { font-size: 27px; line-height: 34px; }
  .person__role { font-size: 15px; margin-top: 6px; }
  .divider {
    position: absolute; left: 30px; right: 28px; top: 141px; height: 2px; background: var(--red);
  }
  .contact { position: absolute; left: 88px; top: 166px; font-size: 14px; line-height: 19px; }
  .contact__icon { position: absolute; left: 85px; top: 178px; }
  .base-band {
    position: absolute; left: 0; bottom: 0; width: 100%; height: 25px;
    background: linear-gradient(90deg, var(--red), var(--red-deep));
  }
</style>
</head>
<body>

<section class="card card--back" aria-label="Card back">
  <div class="brand">
    <span class="brand__dot"></span>
    <span class="brand__name">Brightvane Contracting</span>
  </div>
  <p class="brand__tagline">Providing Effective Project Controls and Management Solutions</p>
  <div class="sectors">
    <p class="sectors__lead">SUPPORTING CLIENTS IN</p>
    <p class="sectors__list">Oil &amp; Gas I Minerals &amp; Metals I Petrochemical I Manufacturing</p>
    <p>Building &amp; Construction I Telecommunication I Rail I Civil I New Industries</p>
  </div>
  <p class="values">KNOWLEDGE I EXPERTISE I EXPERIENCE I CAPACITY</p>
</section>

<section class="card card--front" aria-label="Card front">
  <div class="brand">
    <span class="brand__dot"></span>
    <span class="brand__name">Brightvane Contracting</span>
  </div>
  <p class="brand__tagline">Providing Effective Project Controls and Management Solutions</p>
  <div class="person">
    <p class="person__name">Marcus Feld</p>
    <p class="person__role">Director</p>
  </div>
  <div class="divider"></div>
  <svg class="contact__icon" width="36" height="36" viewBox="0 0 36 36" aria-hidden="true">
    <circle cx="18" cy="18" r="15" fill="none" stroke="var(--red)" stroke-width="3"/>
    <path d="M14 10 L22 18 L14 26" fill="none" stroke="var(--red)" stroke-width="4" stroke-linecap="round" stroke-linejoin="round"/>
  </svg>
  <div class="contact" style="left:130px">
    <p>+61 0497365128</p>
    <p>www.brightvanecontracting.com.au</p>
    <p>marcusfeld@brightvanecontracting.com.au</p>
  </div>
  <div class="base-band"></div>
</section>

</body>
</html>
```